New Architectural Firm Business Cards

New Business card to compliment previous pixel forum logo (attached). Please design a business card that is simple, modern, creative....please do not use "symbols", simply the logo and associated graphics/text. The front should contain name/address/phone/email/web address (with graphics).....back should be 100% graphic design using the logo somehow. Hoping for a two color (black and yellow) design. full bleed design, no borders

Target Market(s)

Commercial Architecture Clients

Industry/Entity Type

Architecture

Contact Information for Business Card

Please design a business card that is simple, modern, creative....please do not use "symbols", simply the logo and associated graphics/text. The front should contain name/address/phone/email/web address (with graphics).....back should be 100% graphic design using the logo somehow

Font styles to use
Sans Serif

Colors
FFF300
FFF600
FEFA6F
FFFEC7
FFFEE8

Requirements
Must have
• Clean, Modern Design
Should not have
• Stock images or "icons"

```html
<!DOCTYPE html>
<html lang="en">
<head>
<meta charset="utf-8">
<title>Pixel Forum Architecture — Business Card</title>
<link rel="stylesheet" href="https://fonts.googleapis.com/css2?family=Montserrat:wght@400;700&family=Roboto+Condensed:wght@700&display=swap">
<style>
  :root {
    --yellow: #f6c416;
    --black: #060708;
    --white: #ffffff;
    --page: #ffffff;
  }
  * { margin: 0; padding: 0; box-sizing: border-box; }
  html, body {
    width: 1066px;
    height: 1200px;
    overflow: hidden;
    background: var(--page);
  }
  .sheet {
    width: 1066px;
    height: 1200px;
    display: flex;
    flex-direction: column;
    align-items: center;
    justify-content: center;
    gap: 64px;
  }
  .card {
    position: relative;
    width: 800px;
    height: 457px;
    background: var(--black);
    overflow: hidden;
  }

  /* Front */
  .card-front .band {
    position: absolute;
    top: 0; bottom: 0; left: 0;
    width: 181px;
    background: var(--yellow);
  }
  .card-front .stripe {
    position: absolute;
    top: 0; bottom: 0;
    left: 200px;
    width: 18px;
    background: var(--yellow);
  }
  .card-front .details {
    position: absolute;
    left: 368px;
    top: 98px;
    font-family: "Montserrat", sans-serif;
  }
  .contact-name {
    color: var(--yellow);
    font-weight: 700;
    font-size: 37px;
    line-height: 1;
    letter-spacing: 0.5px;
    text-transform: uppercase;
  }
  .contact-role {
    color: var(--white);
    font-weight: 400;
    font-size: 18px;
    line-height: 1;
    margin-top: 6px;
    text-transform: uppercase;
  }
  .contact-list {
    list-style: none;
    margin-top: 32px;
  }
  .contact-list li {
    display: flex;
    align-items: center;
    gap: 16px;
    height: 26px;
    margin-bottom: 19px;
    color: var(--yellow);
    font-size: 17.5px;
    font-weight: 400;
    text-transform: uppercase;
    white-space: nowrap;
  }
  .contact-list svg {
    width: 26px;
    height: 26px;
    flex: none;
  }

  /* Back */
  .card-back {
    display: flex;
    flex-direction: column;
    align-items: center;
    justify-content: center;
  }
  .brand-name {
    display: flex;
    align-items: center;
    gap: 18px;
    color: var(--yellow);
    font-family: "Montserrat", sans-serif;
    font-weight: 700;
    font-size: 64px;
    line-height: 1;
    text-transform: uppercase;
    white-space: nowrap;
  }
  .brand-dot {
    width: 30px;
    height: 30px;
    border-radius: 50%;
    background: var(--yellow);
  }
  .brand-descriptor {
    margin-top: 22px;
    color: var(--white);
    font-family: "Roboto Condensed", sans-serif;
    font-weight: 700;
    font-size: 34px;
    letter-spacing: 0.5px;
    text-transform: uppercase;
  }
</style>
</head>
<body>
<main class="sheet">

  <section class="card card-front" aria-label="Business card front">
    <div class="band"></div>
    <div class="stripe"></div>
    <div class="details">
      <h1 class="contact-name">Pixel Forum</h1>
      <p class="contact-role">Pixelforum</p>
      <ul class="contact-list">
        <li>
          <svg viewBox="0 0 26 26" aria-hidden="true">
            <circle cx="13" cy="13" r="13" fill="#fff"/>
            <path d="M13 6a4.6 4.6 0 0 0-4.6 4.6c0 3.4 4.6 8.6 4.6 8.6s4.6-5.2 4.6-8.6A4.6 4.6 0 0 0 13 6z" fill="#060708"/>
            <circle cx="13" cy="10.6" r="1.7" fill="#fff"/>
          </svg>
          Location Lorem Ipsum
        </li>
        <li>
          <svg viewBox="0 0 26 26" aria-hidden="true">
            <circle cx="13" cy="13" r="13" fill="#fff"/>
            <rect x="9" y="6" width="8" height="14" rx="1.5" fill="#060708"/>
            <rect x="10.5" y="8" width="5" height="9" fill="#fff"/>
          </svg>
          +44 70350 2614
        </li>
        <li>
          <svg viewBox="0 0 26 26" aria-hidden="true">
            <circle cx="13" cy="13" r="13" fill="#fff"/>
            <g fill="none" stroke="#060708" stroke-width="1.3">
              <circle cx="13" cy="13" r="7"/>
              <ellipse cx="13" cy="13" rx="3" ry="7"/>
              <line x1="6" y1="13" x2="20" y2="13"/>
              <path d="M7.5 9.5h11M7.5 16.5h11"/>
            </g>
          </svg>
          www.website.com
        </li>
        <li>
          <svg viewBox="0 0 26 26" aria-hidden="true">
            <circle cx="13" cy="13" r="13" fill="#fff"/>
            <rect x="6.5" y="8.5" width="13" height="9" rx="1" fill="#060708"/>
            <path d="M7.5 9.5 13 14l5.5-4.5" fill="none" stroke="#fff" stroke-width="1.3"/>
          </svg>
          email@website.com
        </li>
      </ul>
    </div>
  </section>

  <section class="card card-back" aria-label="Business card back">
    <p class="brand-name"><span class="brand-dot"></span>Pixel Forum</p>
    <p class="brand-descriptor">Architecture</p>
  </section>

</main>
</body>
</html>
```